BEACON CABS

Taxi card design

Need changes very slow in replying to my messages.

Target Market(s)

Customers

Industry/Entity Type

Taxi

Contact Information for Business Card

See previous design

Font styles to use
Sans Serif

Colors
A7469A
B969AE
D3A5CF
EDDBEB
F8F0F9
6B429C
8869AF
B7A5CE
E3DAEB
F3F0F8

Requirements
Nice to have
• We are in the business of looking after people, not just driving vehicles front
Should not have
• Front number 01632 480 480 needs to big big

```html
<!DOCTYPE html>
<html lang="en">
<head>
<meta charset="utf-8">
<title>Beacon Cabs – Business Card</title>
<link rel="stylesheet" href="https://fonts.googleapis.com/css2?family=Poppins:wght@400;500;600;700&display=swap">
<style>
  :root {
    --backdrop: #d3d3d3;
    --card: #ffffff;
    --ink: #1b1b1b;
    --plum-deep: #4a2470;
    --plum: #6b429c;
    --magenta: #922a8c;
    --orchid: #a7469a;
    --orchid-light: #b969ae;
  }
  * { box-sizing: border-box; margin: 0; padding: 0; }
  html, body { width: 1200px; height: 1200px; overflow: hidden; }
  body {
    background: var(--backdrop);
    font-family: "Poppins", sans-serif;
    color: var(--ink);
    position: relative;
  }
  .card {
    position: absolute;
    left: 215px;
    width: 800px;
    height: 480px;
    background: var(--card);
    overflow: hidden;
  }
  .card--front { top: 101px; }
  .card--back { top: 618px; }
  .wave { position: absolute; inset: 0; width: 800px; height: 480px; }
  .text { position: absolute; line-height: 1; white-space: nowrap; }
  .icon {
    position: absolute;
    width: 32px; height: 32px;
    border-radius: 50%;
    background: var(--magenta);
    display: flex; align-items: center; justify-content: center;
  }
  .icon svg { width: 18px; height: 18px; }

  /* front */
  .front-phone { left: 596px; top: 43px; font-size: 25px; font-weight: 500; }
  .front-phone-icon { left: 556px; top: 34px; }
  .brand-name { font-weight: 700; letter-spacing: -0.5px; }
  .front-brand { left: 257px; top: 222px; width: 488px; text-align: center; font-size: 62px; }
  .front-est { left: 257px; top: 279px; font-size: 21px; font-weight: 500; }
  .front-hours { left: 572px; top: 303px; font-size: 22px; font-weight: 700; }
  .front-web { left: 364px; top: 425px; font-size: 25px; }
  .front-web-icon { left: 330px; top: 421px; }

  /* back */
  .back-brand { left: 58px; top: 75px; font-size: 40px; }
  .back-est { left: 60px; top: 111px; font-size: 16px; font-weight: 500; }
  .back-hours { left: 278px; top: 125px; font-size: 15px; font-weight: 700; }
  .services { position: absolute; left: 0; top: 160px; width: 276px; list-style: none; }
  .service {
    height: 32px; margin-bottom: 3px;
    background: linear-gradient(90deg, var(--plum-deep), var(--orchid));
    border-radius: 0 5px 5px 0;
    color: #fff; font-weight: 600; font-size: 19px;
    display: flex; align-items: center; padding-left: 28px; line-height: 1;
  }
  .service::before {
    content: ""; width: 8px; height: 8px; border-radius: 50%;
    background: #fff; margin-right: 10px;
  }
  .phones-icon { left: 41px; top: 281px; }
  .phone-list { position: absolute; left: 86px; top: 285px; font-size: 24px; font-weight: 500; line-height: 29.5px; }
  .email-icon { left: 41px; top: 412px; }
  .email { left: 82px; top: 417px; font-size: 24px; }
  .free-icon { left: 444px; top: 291px; }
  .freephone {
    position: absolute; left: 486px; top: 291px; width: 314px; height: 33px;
    background: linear-gradient(90deg, var(--orchid), var(--plum-deep));
    color: #fff; font-weight: 600; font-size: 20px;
    display: flex; align-items: center; padding-left: 12px; line-height: 1;
  }
  .home-icon { left: 444px; top: 330px; }
  .address { position: absolute; left: 486px; top: 334px; font-size: 23px; font-weight: 500; line-height: 28.5px; font-style: normal; }
</style>
</head>
<body>

<section class="card card--front">
  <svg class="wave" viewBox="0 0 800 480" aria-hidden="true">
    <defs>
      <linearGradient id="waveFront" x1="0" x2="1" y1="0" y2="0">
        <stop offset="0" stop-color="#4a2470"/>
        <stop offset="1" stop-color="#922a8c"/>
      </linearGradient>
      <linearGradient id="waveFrontInner" x1="0" x2="1" y1="0" y2="0">
        <stop offset="0" stop-color="#3f2266"/>
        <stop offset="1" stop-color="#8a2888"/>
      </linearGradient>
    </defs>
    <path d="M0,0 L323,0 C340,90 280,170 190,250 C120,310 85,370 95,420 C98,450 100,470 101,480 L0,480 Z" fill="url(#waveFront)"/>
    <path d="M183,0 L323,0 C340,90 280,170 190,250 C120,310 85,370 95,420 C98,450 100,470 101,480 C60,450 45,400 50,340 C55,290 75,260 100,230 C150,160 185,90 183,0 Z" fill="url(#waveFrontInner)"/>
  </svg>

  <span class="icon front-phone-icon" aria-hidden="true">
    <svg viewBox="0 0 24 24"><path fill="#fff" d="M6.6 10.8c1.4 2.8 3.8 5.1 6.6 6.6l2.2-2.2c.3-.3.7-.4 1-.2 1.1.4 2.3.6 3.6.6.6 0 1 .4 1 1V20c0 .6-.4 1-1 1C10.6 21 3 13.4 3 4c0-.6.4-1 1-1h3.5c.6 0 1 .4 1 1 0 1.3.2 2.5.6 3.6.1.3 0 .7-.2 1z"/></svg>
  </span>
  <p class="text front-phone">01632 480 480</p>

  <h1 class="text brand-name front-brand">Beacon Cabs</h1>
  <p class="text front-est">Established since 1986</p>
  <p class="text front-hours">24/7 Service</p>

  <span class="icon front-web-icon" aria-hidden="true">
    <svg viewBox="0 0 24 24" fill="none" stroke="#fff" stroke-width="1.6"><circle cx="12" cy="12" r="9"/><ellipse cx="12" cy="12" rx="4" ry="9"/><path d="M3 12h18M5 7h14M5 17h14"/></svg>
  </span>
  <p class="text front-web">www.beaconcabs.co.uk</p>
</section>

<section class="card card--back">
  <svg class="wave" viewBox="0 0 800 480" aria-hidden="true">
    <defs>
      <linearGradient id="waveBack" x1="0" x2="1" y1="0" y2="0">
        <stop offset="0" stop-color="#922a8c"/>
        <stop offset="1" stop-color="#6b2a86"/>
      </linearGradient>
      <linearGradient id="waveBackInner" x1="0" x2="0" y1="0" y2="1">
        <stop offset="0" stop-color="#7a2a88"/>
        <stop offset="1" stop-color="#4a2470"/>
      </linearGradient>
    </defs>
    <path d="M567,0 C555,80 620,140 690,190 C740,225 780,250 800,270 L800,0 Z" fill="url(#waveBack)"/>
    <path d="M651,0 C645,70 690,130 740,180 C770,210 790,235 800,255 L800,0 Z" fill="url(#waveBackInner)"/>
  </svg>

  <h2 class="text brand-name back-brand">Beacon Cabs</h2>
  <p class="text back-est">Established since 1986</p>
  <p class="text back-hours">24/7 Service</p>

  <ul class="services">
    <li class="service">AIRPORT TRANSFERS</li>
    <li class="service">MINIBUSES</li>
    <li class="service">SCHOOL TRANSPORT</li>
  </ul>

  <span class="icon phones-icon" aria-hidden="true">
    <svg viewBox="0 0 24 24"><path fill="#fff" d="M6.6 10.8c1.4 2.8 3.8 5.1 6.6 6.6l2.2-2.2c.3-.3.7-.4 1-.2 1.1.4 2.3.6 3.6.6.6 0 1 .4 1 1V20c0 .6-.4 1-1 1C10.6 21 3 13.4 3 4c0-.6.4-1 1-1h3.5c.6 0 1 .4 1 1 0 1.3.2 2.5.6 3.6.1.3 0 .7-.2 1z"/></svg>
  </span>
  <p class="phone-list">01632 480 480<br>01632 79 41 41<br>01632 30 30 30<br>01632 79 55 22</p>

  <span class="icon email-icon" aria-hidden="true">
    <svg viewBox="0 0 24 24" fill="none" stroke="#fff" stroke-width="1.8"><rect x="3" y="6" width="18" height="13" rx="1.5"/><path d="M3 7l9 7 9-7"/></svg>
  </span>
  <p class="text email">beaconcabs@mailbox.co.uk</p>

  <span class="icon free-icon" aria-hidden="true">
    <svg viewBox="0 0 24 24"><path fill="#fff" d="M6.6 10.8c1.4 2.8 3.8 5.1 6.6 6.6l2.2-2.2c.3-.3.7-.4 1-.2 1.1.4 2.3.6 3.6.6.6 0 1 .4 1 1V20c0 .6-.4 1-1 1C10.6 21 3 13.4 3 4c0-.6.4-1 1-1h3.5c.6 0 1 .4 1 1 0 1.3.2 2.5.6 3.6.1.3 0 .7-.2 1z"/></svg>
  </span>
  <p class="freephone">Freephone: 0808 157 0 480</p>

  <span class="icon home-icon" aria-hidden="true">
    <svg viewBox="0 0 24 24"><path fill="#fff" d="M12 3l9 8h-3v9h-4v-6h-4v6H6v-9H3z"/></svg>
  </span>
  <address class="address">Millbrook Chapel Hall<br>Carter Lane<br>Harbridge<br>HB4 7QT</address>
</section>

</body>
</html>
```